R. Tanford Realty, Inc business card (2 sided), letterhead (1 sided) & #10 envelope (1 sided)

business card of standard size utilizing the attached logo. Side one with logo, Wade Tanford (my name), President / Broker (title), 805-555-0183 (phone), www.rtanfordrealty.example (website), 1726 Pelham Avenue, Suite 4403 San Luis Obiso, CA 93401 (business address) wade.rtanfordrealty@mailbox.example (e-mail address),
Side two - Log

Letterhead and #10 envelope in the same theme

Project Deadline Extended
Reason: I think a 2 day deadline may be a bit ambitious on my part. I have extended the deadline to 4 days. Thanks!

```html
<!DOCTYPE html>
<html lang="en">
<head>
<meta charset="utf-8">
<title>R. Tanford Realty, Inc – Stationery Set</title>
<link href="https://fonts.googleapis.com/css2?family=Open+Sans:wght@400;600;700&display=swap" rel="stylesheet">
<style>
  :root{
    --stage:#4a4b4d;
    --paper:#ffffff;
    --teal-dark:#0d4560;
    --teal-mid:#135a7c;
    --teal-light:#1c82b8;
    --brand:#1d5f86;
    --ink:#3d3d3f;
    --rule:#3a3a3c;
    --hairline:#c9cacc;
  }
  *{margin:0;padding:0;box-sizing:border-box}
  html,body{width:1200px;height:755px;overflow:hidden;background:var(--stage);font-family:"Open Sans",Arial,sans-serif}
  .canvas{position:relative;width:1200px;height:755px}
  .piece{position:absolute;background:var(--paper);overflow:hidden}
  .band{position:absolute;left:0;right:0;background:linear-gradient(90deg,var(--teal-dark) 0%,var(--teal-mid) 20%,var(--teal-light) 50%,var(--teal-mid) 80%,var(--teal-dark) 100%);color:#fff;white-space:nowrap}
  .brand-name{position:absolute;display:flex;align-items:center;gap:6px;font-weight:600;color:var(--brand);white-space:nowrap}
  .brand-name .mark{display:inline-block;flex:none;background:var(--brand)}
  .brand-name.on-dark{color:#fff}
  .brand-name.on-dark .mark{background:#fff}

  /* Letterhead */
  .letterhead{left:49px;top:72px;width:478px;height:618px}
  .letterhead .brand-name{left:14px;top:30px;font-size:15px}
  .letterhead .brand-name .mark{width:10px;height:10px}
  .contact{position:absolute;left:350px;top:16px;border-left:1px solid var(--hairline);padding-left:5px;font-size:7px;line-height:13px;color:var(--ink);white-space:nowrap}
  .contact .ico{display:inline-block;width:6px;height:6px;border-radius:50%;background:var(--brand);margin-right:3px;vertical-align:-0.5px}
  .letterhead .watermark{position:absolute;left:78px;top:280px;font-size:26px;font-weight:600;color:#dde4ec;white-space:nowrap}
  .letterhead .rule{position:absolute;left:0;right:0;top:584px;height:2px;background:var(--rule)}
  .letterhead .band{top:588px;height:30px;font-size:8.5px;text-align:center;line-height:30px;letter-spacing:.2px}

  /* Envelope back */
  .envelope-back{left:600px;top:77px;width:533px;height:231px}
  .envelope-back svg{position:absolute;left:0;top:0}
  .envelope-back .brand-name{left:214px;top:28px;font-size:12px}
  .envelope-back .brand-name .mark{width:8px;height:8px}

  /* Envelope front */
  .envelope-front{left:558px;top:160px;width:557px;height:342px;background:none}
  .envelope-front .sheet{position:absolute;background:var(--paper)}
  .envelope-front .flap{position:absolute;left:0;top:0}
  .envelope-front .flap-name{left:214px;top:32px;font-size:12px}
  .envelope-front .flap-name .mark{width:8px;height:8px}
  .envelope-front .return-name{left:46px;top:148px;font-size:13px}
  .envelope-front .return-name .mark{width:9px;height:9px}
  .envelope-front .return-address{position:absolute;left:46px;top:196px;font-size:8.5px;color:var(--ink);letter-spacing:.3px;white-space:nowrap}
  .envelope-front .rule{position:absolute;left:24px;right:0;height:1px;background:var(--rule)}
  .envelope-front .band{left:24px;top:314px;height:28px;font-size:9px;line-height:28px;padding-left:22px;letter-spacing:1.6px}

  /* Business card front */
  .card-front{left:561px;top:565px;width:197px;height:113px}
  .card-front .brand-name{left:10px;top:38px;width:84px;font-size:9px;line-height:11px;gap:4px;white-space:normal}
  .card-front .brand-name .mark{width:6px;height:6px}
  .card-front .divider{position:absolute;left:100px;top:22px;width:1px;height:54px;background:var(--hairline)}
  .card-front .person{position:absolute;left:105px;top:22px;width:88px;color:var(--ink);font-size:4.4px;line-height:9px;white-space:nowrap}
  .card-front .person .name{font-size:8px;font-weight:700;color:var(--brand);line-height:10px}
  .card-front .person .title{font-size:5.5px;line-height:10px;margin-bottom:2px}
  .card-front .person .ico{display:inline-block;width:4px;height:4px;border-radius:50%;background:var(--brand);margin-right:2px;vertical-align:-0.5px}
  .card-front .band{top:99px;height:14px;font-size:5px;line-height:14px;padding-left:36px;background:linear-gradient(90deg,var(--teal-dark),var(--teal-mid) 50%,var(--teal-dark))}
  .card-front .rule{position:absolute;left:0;right:0;top:97px;height:1px;background:var(--rule)}
  .card-front .badge{position:absolute;right:6px;top:100px;width:11px;height:11px;background:#fff;border:1.5px solid #222}

  /* Business card back */
  .card-back{left:778px;top:555px;width:211px;height:127px;background:radial-gradient(ellipse at 50% 45%,#1a6f9c 0%,var(--teal-mid) 45%,var(--teal-dark) 100%)}
  .card-back .brand-name{left:0;right:0;justify-content:center;top:50px;font-size:12px}
  .card-back .brand-name .mark{width:8px;height:8px}
  .card-back .web{position:absolute;left:0;right:0;top:99px;text-align:center;font-size:6.5px;color:#fff;letter-spacing:1px}
</style>
</head>
<body>
<div class="canvas">

  <section class="piece letterhead" aria-label="Letterhead">
    <div class="brand-name"><span class="mark"></span>R. Tanford Realty, Inc</div>
    <div class="contact">
      <div><span class="ico"></span>805-555-0183</div>
      <div><span class="ico"></span>office@rtanfordrealty.example</div>
      <div><span class="ico"></span>www.rtanfordrealty.example</div>
      <div>BRE License # 02486517</div>
    </div>
    <div class="watermark">R. Tanford Realty, Inc</div>
    <div class="rule"></div>
    <div class="band">1726 Pelham Avenue, Suite 4403, San Luis Obispo, CA 93401</div>
  </section>

  <section class="piece envelope-back" aria-label="Envelope back">
    <svg width="533" height="231" viewBox="0 0 533 231">
      <path d="M1 1 L10 80 L10 228" fill="none" stroke="#c9cacc" stroke-width="1"/>
      <path d="M532 1 L523 80 L523 228" fill="none" stroke="#c9cacc" stroke-width="1"/>
      <line x1="0" y1="72" x2="533" y2="72" stroke="#e2e3e5" stroke-width="1"/>
    </svg>
    <div class="brand-name"><span class="mark"></span>R. Tanford Realty, Inc</div>
  </section>

  <section class="piece envelope-front" aria-label="Envelope front">
    <div class="sheet" style="left:0;top:72px;width:532px;height:160px"></div>
    <div class="sheet" style="left:24px;top:148px;width:533px;height:194px"></div>
    <svg class="flap" width="534" height="74" viewBox="0 0 534 74">
      <defs>
        <linearGradient id="flapFill" x1="0" x2="1" y1="0" y2="0">
          <stop offset="0" stop-color="#0d4560"/>
          <stop offset=".5" stop-color="#1c7fb3"/>
          <stop offset="1" stop-color="#0d4560"/>
        </linearGradient>
      </defs>
      <polygon points="0,0 534,0 522,72 12,72" fill="url(#flapFill)"/>
    </svg>
    <div class="brand-name on-dark flap-name"><span class="mark"></span>R. Tanford Realty, Inc</div>
    <div class="brand-name return-name"><span class="mark"></span>R. Tanford Realty, Inc</div>
    <div class="return-address">1726 Pelham Avenue, Suite 4403, San Luis Obispo, CA 93401</div>
    <div class="rule" style="top:308px"></div>
    <div class="rule" style="top:311px"></div>
    <div class="band">www.rtanfordrealty.example</div>
  </section>

  <section class="piece card-front" aria-label="Business card front">
    <div class="brand-name"><span class="mark"></span><span>R. Tanford Realty, Inc</span></div>
    <div class="divider"></div>
    <div class="person">
      <div class="name">Wade Tanford</div>
      <div class="title">President / Broker</div>
      <div><span class="ico"></span>805-555-0183</div>
      <div><span class="ico"></span>wade.rtanfordrealty@mailbox.example</div>
      <div><span class="ico"></span>www.rtanfordrealty.example</div>
      <div>BRE License # 02486517</div>
    </div>
    <div class="rule"></div>
    <div class="band">1726 Pelham Avenue, Suite 4403, San Luis Obispo, CA 93401</div>
    <div class="badge"></div>
  </section>

  <section class="piece card-back" aria-label="Business card back">
    <div class="brand-name on-dark"><span class="mark"></span>R. Tanford Realty, Inc</div>
    <div class="web">www.rtanfordrealty.example</div>
  </section>

</div>
</body>
</html>
```